New sauce/condiment range label design

We need label design for bottles. Its a new range encompassing meat sauce, aioli type dressing, dessert sauce, vinaigrette etc.
The products will be sold in retail gourmet food outlets. They will appeal to a wide range of customers and be purchased for own use as well as gifts.

Reason: I'm away from email for this period so no need to hurry over this one! Thanks

Target Market(s)

pretty much everyone over 20yrs of age who appreciate great tasting foods

Industry/Entity Type

Retail

Requirements
Must have
• Must have company name, fern logo (which can be seperated from name and also different colours.
The label dimensions are 50mm high x 190mm wide.

```html
<!DOCTYPE html>
<html lang="en">
<head>
<meta charset="utf-8">
<title>Harbour Pantry – Sauce Range Labels</title>
<link rel="stylesheet" href="https://fonts.googleapis.com/css2?family=Arimo:wght@400;700&family=Tinos&display=swap">
<style>
  :root {
    --page: #ffffff;
    --label-cream: #efece4;
    --ink: #1d1d1d;
    --ink-soft: #8a8a86;
    --rule: #2a2a2a;
    --meat-red: #b5151f;
    --meat-lime: #9ec424;
    --seafood-blue: #1f2c8e;
    --band-text: #ffffff;
  }
  * { box-sizing: border-box; margin: 0; padding: 0; }
  html, body {
    width: 1200px;
    height: 750px;
    overflow: hidden;
    background: var(--page);
  }
  .range {
    width: 1200px;
    height: 750px;
    display: flex;
    align-items: center;
    justify-content: center;
    gap: 30px;
  }
  .label {
    position: relative;
    width: 360px;
    height: 290px;
    background: var(--label-cream);
    font-family: "Arimo", Arial, sans-serif;
    color: var(--ink);
    box-shadow: 0 1px 3px rgba(0,0,0,0.12);
  }
  .label--red { --accent: var(--meat-red); }
  .label--lime { --accent: var(--meat-lime); }
  .label--blue { --accent: var(--seafood-blue); }

  .label__tagline {
    position: absolute;
    left: 34px;
    top: 26px;
    font-size: 13px;
    font-weight: 700;
  }
  .label__brand {
    position: absolute;
    left: 24px;
    top: 44px;
    font-size: 27px;
    font-weight: 400;
    letter-spacing: -0.2px;
  }
  .label__mark {
    position: absolute;
    left: 30px;
    top: 112px;
    width: 84px;
    height: 84px;
  }
  .label__product {
    position: absolute;
    left: 140px;
    top: 100px;
    width: 200px;
  }
  .label__product-name {
    font-family: "Tinos", "Times New Roman", serif;
    font-weight: 400;
    font-size: 42px;
    line-height: 1;
    letter-spacing: -0.5px;
    padding: 8px 0 6px;
    border-top: 1.5px solid var(--rule);
    border-bottom: 1.5px solid var(--rule);
    text-transform: uppercase;
    width: 170px;
  }
  .label__descriptor {
    margin-top: 10px;
    font-size: 13px;
    color: var(--ink-soft);
    word-spacing: 2px;
  }
  .label__band {
    position: absolute;
    left: 0;
    right: 0;
    bottom: 22px;
    height: 32px;
    background: var(--accent);
    color: var(--band-text);
    font-size: 12px;
    display: flex;
    align-items: center;
    justify-content: space-between;
    padding: 0 12px;
  }
</style>
</head>
<body>
<main class="range">

  <article class="label label--red">
    <p class="label__tagline">bringing joy to your tastebuds!</p>
    <h2 class="label__brand">Harbour Pantry</h2>
    <svg class="label__mark" viewBox="0 0 84 84" aria-hidden="true">
      <circle cx="42" cy="42" r="40" fill="var(--meat-red)"/>
    </svg>
    <div class="label__product">
      <h1 class="label__product-name">Meat<br>Sauce</h1>
      <p class="label__descriptor">Loremp Ipsum sit amet</p>
    </div>
    <footer class="label__band">
      <span>Made in New Zealand</span>
      <span>NET WT 12 oz (355ml)</span>
    </footer>
  </article>

  <article class="label label--lime">
    <p class="label__tagline">bringing joy to your tastebuds!</p>
    <h2 class="label__brand">Harbour Pantry</h2>
    <svg class="label__mark" viewBox="0 0 84 84" aria-hidden="true">
      <circle cx="42" cy="42" r="40" fill="var(--meat-lime)"/>
    </svg>
    <div class="label__product">
      <h1 class="label__product-name">Meat<br>Sauce</h1>
      <p class="label__descriptor">Loremp Ipsum sit amet</p>
    </div>
    <footer class="label__band">
      <span>Made in New Zealand</span>
      <span>NET WT 12 oz (355ml)</span>
    </footer>
  </article>

  <article class="label label--blue">
    <p class="label__tagline">bringing joy to your tastebuds!</p>
    <h2 class="label__brand">Harbour Pantry</h2>
    <svg class="label__mark" viewBox="0 0 84 84" aria-hidden="true">
      <circle cx="42" cy="42" r="40" fill="var(--seafood-blue)"/>
    </svg>
    <div class="label__product">
      <h1 class="label__product-name">Seafood<br>Sauce</h1>
      <p class="label__descriptor">Loremp Ipsum sit amet</p>
    </div>
    <footer class="label__band">
      <span>Made in New Zealand</span>
      <span>NET WT 12 oz (355ml)</span>
    </footer>
  </article>

</main>
</body>
</html>
```